Tavola coffee shop
Tavola Cafe'
To all designer : please try to make idea to add food items in the future which will not affect the design
All designer : i hope when we start the menu to start with the coffee section then juice section then........
All Designer , no need to stick to the same dimenssion that i gave u . you can prpose any dimenssion
Dear All
the Uploaded attachment is only an example and not to copy the same design
Dear all
My coffee shop logo is the arabic name and not the circle
to have good start, we need to show in our design the layout of the writing and not to copy the word format file and past it in the design. in addtion this boklet my be 4 page exluding the cover page
i need the menu to be as booklet
the size of the paper is 21.2cmX27.9cm

```html
<!DOCTYPE html>
<html lang="en">
<head>
<meta charset="utf-8">
<title>Tavola Cafe' – Menu Booklet</title>
<link href="https://fonts.googleapis.com/css2?family=Open+Sans:wght@400;600;700&family=Cairo:wght@400;700&display=swap" rel="stylesheet">
<style>
  :root {
    --backdrop-light: #9a9a9a;
    --backdrop-dark: #6c6c6c;
    --red-core: #d3222b;
    --red-mid: #b0131b;
    --red-edge: #7a0a10;
    --gold: #f2c14e;
    --gold-soft: rgba(242, 193, 78, 0.4);
    --text-light: #ffffff;
    --text-muted: #f4d7d7;
    --frame-white: #ffffff;
    --rule: rgba(255, 255, 255, 0.35);
  }
  * { box-sizing: border-box; margin: 0; padding: 0; }
  html, body { width: 1200px; height: 446px; overflow: hidden; }
  body {
    position: relative;
    background: linear-gradient(180deg, var(--backdrop-light), var(--backdrop-dark));
    font-family: "Open Sans", Arial, sans-serif;
    color: var(--text-light);
  }
  .page {
    position: absolute;
    top: 36px;
    height: 390px;
    width: 288px;
    background: radial-gradient(ellipse at 50% 45%, var(--red-core) 0%, var(--red-mid) 60%, var(--red-edge) 100%);
    box-shadow: 0 4px 12px rgba(0,0,0,0.45);
    overflow: hidden;
  }
  .page--cover { left: 8px; width: 290px; }
  .page--inner-en { left: 307px; }
  .page--inner-ar { left: 605px; }
  .page--back { left: 903px; width: 290px; }

  .corner-ornament {
    position: absolute;
    width: 60px; height: 60px;
    background: radial-gradient(circle at 0 0, var(--gold-soft), transparent 70%);
  }
  .corner-ornament--tl { top: 0; left: 0; }
  .corner-ornament--tr { top: 0; right: 0; transform: scaleX(-1); }
  .corner-ornament--bl { bottom: 0; left: 0; transform: scaleY(-1); }
  .corner-ornament--br { bottom: 0; right: 0; transform: scale(-1, -1); }

  .cover-brand {
    position: absolute;
    top: 92px; left: 40px; width: 210px;
    text-align: center;
  }
  .cover-brand__name {
    font-family: "Cairo", Arial, sans-serif;
    font-size: 38px; line-height: 50px; font-weight: 700; color: var(--gold);
  }
  .cover-brand__tag {
    margin-top: 4px;
    font-size: 11px; font-weight: 600; color: var(--text-light);
  }

  .brand-mark {
    position: absolute;
    top: 12px; left: 176px;
    font-family: "Cairo", Arial, sans-serif;
    font-size: 13px; line-height: 18px; font-weight: 700; color: var(--gold);
  }

  .photo {
    position: absolute;
    border: 3px solid var(--frame-white);
  }
  .photo--coffee { background: radial-gradient(circle at 50% 50%, #6b3a1e 0%, #a86a3c 30%, #f1e7da 55%, #ddd0c0 100%); }
  .photo--juice { background: linear-gradient(170deg, #f7f1ea 0%, #f5a623 35%, #e0661b 70%, #f3ece3 100%); }
  .photo--burger { background: linear-gradient(180deg, #f3efe6 0%, #c98a3b 22%, #7ea73a 40%, #5b2a15 58%, #d9a53d 72%, #c27c32 88%, #f1ece2 100%); }

  .menu-section {
    position: absolute;
    top: 124px;
    width: 100px;
    font-size: 6.5px;
    line-height: 10px;
  }
  .menu-section__title {
    font-size: 8.5px; line-height: 12px; font-weight: 700; letter-spacing: 0.3px;
    margin-bottom: 3px;
  }
  .menu-item { display: flex; justify-content: space-between; gap: 6px; color: var(--text-muted); }
  .menu-item__name::before { content: "• "; color: var(--gold); }
  .menu-item__price { color: var(--text-light); }

  .section-rule {
    position: absolute;
    left: 20px; top: 214px; width: 248px;
    height: 1px; background: var(--rule);
  }

  .main-dish { position: absolute; top: 230px; left: 134px; width: 134px; font-size: 6.5px; line-height: 9px; }
  .main-dish__title { font-size: 9.5px; line-height: 13px; font-weight: 700; margin-bottom: 4px; }
  .main-dish__head { display: flex; justify-content: space-between; gap: 6px; font-weight: 600; color: var(--text-light); }
  .main-dish__desc { color: var(--text-muted); margin-bottom: 5px; }

  .lang-ar { font-family: "Cairo", Arial, sans-serif; direction: rtl; text-align: right; }

  .back-contact {
    position: absolute;
    left: 55px; top: 268px;
    font-size: 6.5px; line-height: 10px; color: var(--text-muted);
  }
  .back-contact__name { font-size: 10px; line-height: 13px; font-weight: 700; color: var(--text-light); margin-bottom: 4px; }
</style>
</head>
<body>

  <section class="page page--cover">
    <div class="corner-ornament corner-ornament--tr" role="img" aria-label="gold floral corner ornament"></div>
    <div class="corner-ornament corner-ornament--bl" role="img" aria-label="gold floral corner ornament"></div>
    <div class="corner-ornament corner-ornament--br" role="img" aria-label="gold floral corner ornament"></div>
    <div class="cover-brand">
      <div class="cover-brand__name" lang="ar" dir="rtl">تافولا كافيه</div>
      <div class="cover-brand__tag">Tavola Cafe'</div>
    </div>
  </section>

  <section class="page page--inner-en">
    <div class="corner-ornament corner-ornament--tr" role="img" aria-label="gold floral corner ornament"></div>
    <div class="brand-mark">Tavola Cafe'</div>

    <div class="photo photo--coffee" role="img" aria-label="photo of a cup of coffee" style="left:20px; top:46px; width:100px; height:66px;"></div>
    <div class="photo photo--juice" role="img" aria-label="photo of a glass of fresh juice" style="left:128px; top:46px; width:104px; height:66px;"></div>

    <div class="menu-section" style="left:20px;">
      <div class="menu-section__title">COFFEE</div>
      <div class="menu-item"><span class="menu-item__name">Espresso</span><span class="menu-item__price">12dhs</span></div>
      <div class="menu-item"><span class="menu-item__name">Cappuccino</span><span class="menu-item__price">16dhs</span></div>
      <div class="menu-item"><span class="menu-item__name">Caffe latte</span><span class="menu-item__price">16dhs</span></div>
      <div class="menu-item"><span class="menu-item__name">Americano</span><span class="menu-item__price">14dhs</span></div>
      <div class="menu-item"><span class="menu-item__name">Turkish coffee</span><span class="menu-item__price">10dhs</span></div>
    </div>

    <div class="menu-section" style="left:134px;">
      <div class="menu-section__title">FRESH JUICE</div>
      <div class="menu-item"><span class="menu-item__name">Orange</span><span class="menu-item__price">15dhs</span></div>
      <div class="menu-item"><span class="menu-item__name">Mango</span><span class="menu-item__price">18dhs</span></div>
      <div class="menu-item"><span class="menu-item__name">Lemon mint</span><span class="menu-item__price">15dhs</span></div>
      <div class="menu-item"><span class="menu-item__name">Strawberry</span><span class="menu-item__price">18dhs</span></div>
    </div>

    <div class="section-rule"></div>

    <div class="photo photo--burger" role="img" aria-label="photo of beef burger" style="left:20px; top:228px; width:100px; height:122px;"></div>

    <div class="main-dish">
      <div class="main-dish__title">MAIN COURSE</div>
      <div class="main-dish__head"><span>Classic Beef Burger</span><span>35dhs</span></div>
      <div class="main-dish__desc">Grilled beef, cheese, lettuce, tomato, served with fries</div>
      <div class="main-dish__head"><span>Chicken Burger</span><span>32dhs</span></div>
      <div class="main-dish__desc">Crispy chicken, pickles, house sauce, served with fries</div>
      <div class="main-dish__head"><span>Club Sandwich</span><span>30dhs</span></div>
      <div class="main-dish__desc">Turkey, egg, cheese and fresh greens</div>
    </div>
  </section>

  <section class="page page--inner-ar">
    <div class="corner-ornament corner-ornament--tr" role="img" aria-label="gold floral corner ornament"></div>
    <div class="brand-mark">Tavola Cafe'</div>

    <div class="photo photo--coffee" role="img" aria-label="photo of a cup of coffee" style="left:20px; top:46px; width:100px; height:66px;"></div>
    <div class="photo photo--juice" role="img" aria-label="photo of a glass of fresh juice" style="left:128px; top:46px; width:104px; height:66px;"></div>

    <div class="menu-section lang-ar" style="left:168px;">
      <div class="menu-section__title">القهوة</div>
      <div class="menu-item"><span class="menu-item__name">إسبريسو</span><span class="menu-item__price">١٢</span></div>
      <div class="menu-item"><span class="menu-item__name">كابتشينو</span><span class="menu-item__price">١٦</span></div>
      <div class="menu-item"><span class="menu-item__name">لاتيه</span><span class="menu-item__price">١٦</span></div>
      <div class="menu-item"><span class="menu-item__name">أمريكانو</span><span class="menu-item__price">١٤</span></div>
      <div class="menu-item"><span class="menu-item__name">قهوة تركية</span><span class="menu-item__price">١٠</span></div>
    </div>

    <div class="menu-section lang-ar" style="left:54px;">
      <div class="menu-section__title">العصائر الطازجة</div>
      <div class="menu-item"><span class="menu-item__name">برتقال</span><span class="menu-item__price">١٥</span></div>
      <div class="menu-item"><span class="menu-item__name">مانجو</span><span class="menu-item__price">١٨</span></div>
      <div class="menu-item"><span class="menu-item__name">ليمون ونعناع</span><span class="menu-item__price">١٥</span></div>
      <div class="menu-item"><span class="menu-item__name">فراولة</span><span class="menu-item__price">١٨</span></div>
    </div>

    <div class="section-rule"></div>

    <div class="photo photo--burger" role="img" aria-label="photo of beef burger" style="left:20px; top:228px; width:100px; height:122px;"></div>

    <div class="main-dish lang-ar">
      <div class="main-dish__title">الأطباق الرئيسية</div>
      <div class="main-dish__head"><span>برجر لحم كلاسيك</span><span>٣٥</span></div>
      <div class="main-dish__desc">لحم مشوي، جبن، خس وطماطم، يقدم مع البطاطس</div>
      <div class="main-dish__head"><span>برجر دجاج</span><span>٣٢</span></div>
      <div class="main-dish__desc">دجاج مقرمش، مخلل وصلصة خاصة</div>
      <div class="main-dish__head"><span>كلوب ساندويتش</span><span>٣٠</span></div>
      <div class="main-dish__desc">ديك رومي، بيض، جبن وخضار</div>
    </div>
  </section>

  <section class="page page--back">
    <div class="corner-ornament corner-ornament--tr" role="img" aria-label="gold floral corner ornament"></div>
    <div class="corner-ornament corner-ornament--br" role="img" aria-label="gold floral corner ornament"></div>
    <div class="back-contact">
      <div class="back-contact__name">Tavola Cafe'</div>
      <div>Phone: 04 555 0123</div>
      <div>Fax: 04 555 0124</div>
      <div>info@bluequillvon.com</div>
      <div>www.bluequillvon.com</div>
    </div>
  </section>

</body>
</html>
```